Water ATM Card

Need a design for water ATM cards. Size of card is 3.375 x 2.125 inch
On the Front include the Cedar brook Logo.
Bottom right corner should have Price $100
On the Back
This card is to be used to access water refills at any Cedar Brook Water Vending Machines.
Please contact (869) 614 2938 or (869) 731 4072 or email clearflowhq@examplemail.com for any assistance or recharging of card.

```html
<!DOCTYPE html>
<html lang="en">
<head>
<meta charset="utf-8">
<title>Cedar Brook Water ATM Card</title>
<link rel="stylesheet" href="https://fonts.googleapis.com/css2?family=Montserrat:wght@500;600;800&family=Antonio:wght@100&display=swap">
<style>
  :root {
    --bg: #222222;
    --card-dark: #1c1c1c;
    --green-deep: #1f9a48;
    --green-light: #7dc243;
    --green-ink: #0c4420;
    --brand-blue: #1478c0;
    --edge-blue: #2a6fd0;
    --white: #ffffff;
  }
  html, body {
    margin: 0;
    padding: 0;
    overflow: hidden;
  }
  .canvas {
    width: 1200px;
    height: 711px;
    background: var(--bg);
    position: relative;
    overflow: hidden;
  }
  .card {
    position: absolute;
    top: 198px;
    width: 500px;
    height: 315px;
    border-radius: 22px;
    overflow: hidden;
    box-sizing: border-box;
    box-shadow: 0 10px 24px rgba(0,0,0,0.55);
  }
  .card--back {
    left: 60px;
    background: linear-gradient(35deg, var(--green-deep) 0%, var(--green-light) 100%);
    padding: 58px 44px 0;
    text-align: center;
    color: var(--green-ink);
  }
  .card--front {
    left: 640px;
    background: var(--card-dark);
    border-bottom: 3px solid var(--green-deep);
  }
  .brand-name {
    margin: 0;
    text-align: center;
    font-family: "Montserrat", sans-serif;
    font-weight: 800;
    font-size: 42px;
    line-height: 1;
    letter-spacing: 2px;
    text-transform: uppercase;
  }
  .card--back .brand-name {
    color: var(--green-ink);
  }
  .card--front .brand-name {
    position: absolute;
    left: 0;
    right: 0;
    top: 78px;
    color: var(--brand-blue);
  }
  .card-usage,
  .card-contact {
    font-family: "Montserrat", sans-serif;
    font-weight: 500;
    font-size: 14px;
    line-height: 1.5;
    margin: 0;
  }
  .card-usage {
    margin-top: 34px;
  }
  .card-contact {
    margin-top: 14px;
  }
  .card-contact strong {
    font-weight: 500;
    white-space: nowrap;
  }
  .price-band {
    position: absolute;
    inset: 0;
    width: 100%;
    height: 100%;
  }
  .price-label {
    position: absolute;
    left: 292px;
    top: 236px;
    margin: 0;
    font-family: "Antonio", sans-serif;
    font-weight: 100;
    font-size: 36px;
    line-height: 1;
    color: var(--white);
    letter-spacing: 1px;
    transform: rotate(-22deg);
    transform-origin: left bottom;
    white-space: nowrap;
  }
</style>
</head>
<body>
<div class="canvas">
  <section class="card card--back" aria-label="Card back">
    <p class="brand-name">Cedar Brook</p>
    <p class="card-usage">This card is to be used to access water refills at any Cedar Brook Water Vending Machines.</p>
    <p class="card-contact">Please contact <strong>(869) 614 2938</strong> or <strong>(869) 731 4072</strong> or email <strong>clearflowhq@examplemail.com</strong> for any assistance or recharging of card.</p>
  </section>

  <section class="card card--front" aria-label="Card front">
    <svg class="price-band" viewBox="0 0 500 315" preserveAspectRatio="none" aria-hidden="true">
      <defs>
        <linearGradient id="bandGreen" x1="0" y1="1" x2="1" y2="0">
          <stop offset="0" stop-color="#1f9a48"/>
          <stop offset="1" stop-color="#7dc243"/>
        </linearGradient>
      </defs>
      <path d="M205 315 Q330 180 500 150 L500 315 Z" fill="url(#bandGreen)"/>
      <path d="M205 315 Q330 180 500 150" fill="none" stroke="#2a6fd0" stroke-width="5"/>
    </svg>
    <p class="brand-name">Cedar Brook</p>
    <p class="price-label">PRICE $100</p>
  </section>
</div>
</body>
</html>
```